Innovative Consulting Firm Needs New Business Cards and Stationary

Our Innovative Consulting Firm, Harrowgate Consulting, is in need of new business cards and stationary designs. We want two-sided cards that incorporate our logo, which is attached. We are looking for something not too formal, but is professional and slick.

Card should have the following information:
Name (ex. Lena Vork)
Title (ex. Manager)
Address (ex. 24680 Quill Avenue)
Address 2 (ex. Suite 100)
City
State
Zip Code
Mobile
Email

The card should also have our website: www.harrowgateconsulting.example

Industry/Entity Type

Management Consulting

Contact Information for Business Card

Name (ex. Lena Vork)
Title (ex. Manager)
Address 2 (ex. Suite 100)
City
State
Zip Code
Mobile
Email

Font styles to use
Sans Serif

Requirements
Must have
• The colors on the card must match the colors in the logo. The exact color codes are attached in a pdf.
Nice to have
• The Company's Tagline is "Focused on your Future". This might be nice to incorporate, but not necessary.

```html
<!DOCTYPE html>
<html lang="en">
<head>
<meta charset="utf-8">
<title>Harrowgate Consulting – Business Cards</title>
<link href="https://fonts.googleapis.com/css2?family=Open+Sans:wght@400;600;700&display=swap" rel="stylesheet">
<style>
  :root {
    --brand-blue: #1f69a6;
    --brand-blue-deep: #185a92;
    --brand-gold: #e6b220;
    --card-white: #f6f6f4;
    --stage: #e8e5df;
    --text-light: #ffffff;
  }
  * { margin: 0; padding: 0; box-sizing: border-box; }
  html, body { width: 1200px; height: 780px; overflow: hidden; }
  body {
    background: var(--stage);
    font-family: "Open Sans", Arial, sans-serif;
    position: relative;
  }
  .card {
    position: absolute;
    width: 540px;
    height: 309px;
    border-radius: 3px;
    overflow: hidden;
    box-shadow: 0 6px 18px rgba(0,0,0,.18);
  }
  .card-front { left: 60px; top: 70px; background: var(--card-white); }
  .card-back { left: 600px; top: 400px; background: var(--brand-blue); }

  /* brand name block */
  .brand { display: flex; align-items: center; gap: 10px; }
  .brand-dot {
    width: 14px; height: 14px; border-radius: 50%;
    background: var(--brand-gold);
    flex: none;
  }
  .brand-name {
    color: var(--brand-blue);
    font-weight: 600;
    font-size: 34px;
    letter-spacing: 0.5px;
    line-height: 1;
  }
  .brand-sub {
    color: var(--brand-blue);
    font-weight: 400;
    font-size: 13px;
    letter-spacing: 7px;
    text-transform: uppercase;
    margin-top: 6px;
    padding-left: 24px;
  }

  /* front */
  .front-brand { position: absolute; left: 36px; top: 52px; }
  .front-band {
    position: absolute; left: 0; right: 0; top: 170px; height: 108px;
    background: linear-gradient(90deg, var(--brand-blue-deep), var(--brand-blue));
    border-top: 3px solid var(--brand-gold);
    border-bottom: 3px solid var(--brand-gold);
    box-shadow: 0 -6px 0 var(--card-white), 0 -7px 0 var(--brand-gold);
    color: var(--text-light);
    display: flex; justify-content: space-between;
    padding: 14px 22px 0 22px;
  }
  .person-name { font-weight: 700; font-size: 17px; }
  .person-title { font-weight: 400; font-size: 12px; opacity: .9; }
  .person-title::before { content: "|"; margin: 0 6px; opacity: .7; }
  .contact-list { list-style: none; margin-top: 4px; }
  .contact-list li {
    display: flex; align-items: center; gap: 7px;
    font-size: 12px; line-height: 19px;
  }
  .contact-icon {
    width: 13px; height: 13px; background: var(--brand-gold);
    border-radius: 2px; display: flex; align-items: center; justify-content: center;
  }
  .address { font-size: 12px; line-height: 19px; text-align: right; padding-top: 2px; }

  /* back */
  .back-band {
    position: absolute; left: 0; right: 0; top: 78px; height: 153px;
    background: var(--card-white);
    box-shadow: 0 -5px 0 var(--brand-blue), 0 -7px 0 var(--brand-gold),
                0 5px 0 var(--brand-blue), 0 7px 0 var(--brand-gold);
    display: flex; align-items: center; justify-content: center;
  }
</style>
</head>
<body>

<section class="card card-front" aria-label="Business card front">
  <div class="brand-block front-brand">
    <div class="brand">
      <span class="brand-dot"></span>
      <span class="brand-name">Harrowgate</span>
    </div>
    <div class="brand-sub">Consulting</div>
  </div>

  <div class="front-band">
    <div class="contact">
      <p><span class="person-name">Lena Vork</span><span class="person-title">Manager</span></p>
      <ul class="contact-list">
        <li><span class="contact-icon"><svg width="9" height="9" viewBox="0 0 10 10"><path d="M2 1l2 2-1 1.5a6 6 0 0 0 2.5 2.5L7 6l2 2-1.2 1.3C4.5 9 1 5.5.7 2.2z" fill="#185a92"/></svg></span>+61 555 010 284</li>
        <li><span class="contact-icon"><svg width="9" height="9" viewBox="0 0 10 10"><rect x="1" y="2" width="8" height="6" fill="none" stroke="#185a92"/><path d="M1 2l4 3.5L9 2" fill="none" stroke="#185a92"/></svg></span>lena.vork@harrowgate.example</li>
        <li><span class="contact-icon"><svg width="9" height="9" viewBox="0 0 10 10"><circle cx="5" cy="5" r="4" fill="none" stroke="#185a92"/><path d="M1 5h8M5 1c-2 2.5-2 5.5 0 8M5 1c2 2.5 2 5.5 0 8" fill="none" stroke="#185a92" stroke-width=".8"/></svg></span>www.harrowgateconsulting.example</li>
      </ul>
    </div>
    <div class="address">
      <p>24680 Quill Avenue, Suite 100, USA</p>
      <p>24680 Quill Avenue, Suite 100, USA</p>
    </div>
  </div>
</section>

<section class="card card-back" aria-label="Business card back">
  <div class="back-band">
    <div class="brand-block">
      <div class="brand">
        <span class="brand-dot"></span>
        <span class="brand-name">Harrowgate</span>
      </div>
      <div class="brand-sub">Consulting</div>
    </div>
  </div>
</section>

</body>
</html>
```